Bay Bolts

I am starting a sharpening service for knives, scissors, and garden tools. It's a sole proprietorship, so it's a small business. The business name is "Bay Bolt." A one or two-page website is fine. Mark Orchard has created a logo for me. There should be pictures of the things I sharpen. There will also be a price list for sharpened items. My address is: 18302 Pellman Way, Stevenson Ranch, CA 91381. Phone number is 661-555-0173

```html
<!DOCTYPE html>
<html lang="en">
<head>
<meta charset="utf-8">
<title>Bay Bolt — Precision Sharpening</title>
<link href="https://fonts.googleapis.com/css2?family=Oswald:wght@400;500;600&family=Montserrat:wght@400;500;600;700&display=swap" rel="stylesheet">
<style>
:root{
  --red:#d90000;
  --black:#000;
  --ink:#111;
  --grey-bg:#f0f0f0;
  --white:#fff;
  --muted:#444;
  --line:#9a9a9a;
  --field:#e3e3e3;
}
*{box-sizing:border-box;margin:0;padding:0}
html,body{width:1200px;height:4951px;overflow:hidden}
body{font-family:"Montserrat",sans-serif;color:var(--ink);background:var(--grey-bg);position:relative}
section,header,footer{position:absolute;left:0;width:1200px}
.abs{position:absolute}

/* hero */
.hero{top:0;height:567px;background:var(--black);overflow:hidden}
.hero-photo{position:absolute;inset:0;background:radial-gradient(ellipse at 68% 55%,#6a3a14 0%,#2a1a10 30%,#0c0a09 60%,#000 100%)}
.brand{font-family:"Oswald",sans-serif;font-weight:600;color:var(--white);font-size:38px;letter-spacing:2px;line-height:1;text-transform:uppercase}
.nav{top:44px;left:478px;display:flex;gap:24px;font-size:15px;color:var(--white)}
.phone-btn{top:36px;left:922px;width:146px;height:34px;background:var(--red);color:var(--white);font-size:14px;font-weight:700;display:flex;align-items:center;justify-content:center;gap:8px;transform:skewX(-12deg)}
.phone-btn span,.phone-btn svg,.btn span{transform:skewX(12deg)}
.hero-title{top:188px;left:129px;font-family:"Oswald",sans-serif;font-weight:500;font-size:52px;line-height:60px;color:var(--white)}
.hero-text{top:323px;left:129px;width:380px;font-size:14px;line-height:18px;color:var(--white)}
.btn{display:flex;align-items:center;justify-content:center;gap:7px;font-weight:700;font-size:13px;transform:skewX(-12deg)}
.btn-red{background:var(--red);color:var(--white)}
.btn-white{background:var(--white);color:var(--ink)}
.hero-band{top:567px;height:18px;background:var(--red)}

.section-title{width:1200px;text-align:center;font-family:"Oswald",sans-serif;font-weight:500;font-size:40px;color:var(--ink);text-transform:uppercase}

/* sharpen cards */
.sharpen-card{width:300px;background:var(--white);border-radius:8px;overflow:hidden;box-shadow:0 2px 10px rgba(0,0,0,.05)}
.sharpen-card h3{background:var(--red);color:var(--white);font-family:"Oswald",sans-serif;font-weight:500;font-size:25px;text-align:center;height:52px;line-height:52px}
.photo{display:block}
.sharpen-card .lead{font-family:"Oswald",sans-serif;font-size:19px;line-height:24px;margin:14px 26px 16px;color:var(--ink)}
.ticks{list-style:none;margin:0 26px;font-size:14px;line-height:27px;color:var(--muted)}
.ticks li::before{content:"✓ ";color:var(--ink);font-weight:700}

.compare{top:1510px;left:112px;width:957px;height:409px;border-radius:10px;overflow:hidden;background:linear-gradient(90deg,#2c2a28,#3a3835 50%,#2a2826)}
.compare .divider{position:absolute;left:465px;top:0;width:2px;height:409px;background:#111}
.compare .handle{position:absolute;left:446px;top:180px;width:40px;height:40px;border:2px solid #111;border-radius:50%}
.compare .tag{position:absolute;bottom:18px;font-family:"Oswald",sans-serif;font-size:40px;color:var(--white);font-weight:500}

/* price cards */
.price-card{width:300px;height:625px;background:var(--white);border-radius:8px;overflow:hidden;text-align:center}
.price-card h3{background:var(--black);color:var(--white);font-family:"Oswald",sans-serif;font-weight:500;font-size:25px;height:52px;line-height:56px}
.price-card .photo{height:150px}
.price-band{background:var(--red);color:var(--white);font-family:"Oswald",sans-serif;font-size:38px;height:62px;line-height:66px}
.price-band small{font-size:27px}
.deal{font-family:"Oswald",sans-serif;font-weight:500;font-size:42px;line-height:48px;margin-top:12px}
.price-list{list-style:none;margin:16px 36px 0 36px;text-align:left;font-size:14px;color:var(--muted)}
.price-list li{border-bottom:1px solid var(--line);height:46px;display:flex;align-items:flex-end;padding-bottom:6px}
.price-list b{color:var(--red);font-size:19px;margin-left:8px}
.price-card .btn{position:absolute;bottom:18px;left:75px;width:150px;height:36px}

/* testimonial */
.testimonial{top:2925px;height:585px;background:var(--black);color:var(--white)}
.quote{top:182px;left:240px;width:720px;text-align:center;font-weight:700;font-size:37px;line-height:55px}
.arrow{width:40px;height:40px;border:1.5px solid var(--white);border-radius:50%;display:flex;align-items:center;justify-content:center}

/* contact */
.contact-media{left:119px;top:3785px;width:475px;height:638px;background:var(--white);border-radius:8px;overflow:hidden}
.info-icon{width:44px;height:44px;border-radius:50%;background:var(--red);display:flex;align-items:center;justify-content:center}
.info-title{font-family:"Oswald",sans-serif;font-size:17px}
.info-text{font-size:13px;line-height:23px;color:var(--muted)}
.form-card{left:606px;top:3785px;width:473px;height:638px;background:var(--white);border-radius:8px}
.form-card label{position:absolute;font-size:11px;color:var(--ink)}
.field{position:absolute;border:1px solid var(--field);border-radius:6px;font-size:11px;color:#444;padding:12px 12px}

/* footer */
.site-footer{top:4577px;height:323px;background:var(--black);color:var(--white)}
.footer-head{font-family:"Oswald",sans-serif;font-size:19px}
.footer-links{list-style:none;font-size:16px;line-height:38px}
.social{width:20px;height:20px;border:2px solid var(--white);border-radius:4px}
.copyright{top:4900px;height:51px;background:var(--red);color:var(--white);font-size:13px;text-align:center;line-height:51px}
</style>
</head>
<body>

<header class="hero">
  <div class="hero-photo" role="img" aria-label="Close-up of a hand holding a blade against a grinding wheel with orange sparks flying"></div>
  <div class="abs brand" style="top:30px;left:131px">Bay Bolt</div>
  <nav class="abs nav"><span>Home</span><span>About</span><span>Pricing</span><span>Contact</span></nav>
  <div class="abs phone-btn">
    <svg width="14" height="14" viewBox="0 0 24 24" fill="#fff"><path d="M6.6 10.8a15 15 0 0 0 6.6 6.6l2.2-2.2c.3-.3.7-.4 1-.2 1.1.4 2.3.6 3.6.6.6 0 1 .4 1 1V20c0 .6-.4 1-1 1A17 17 0 0 1 3 4c0-.6.4-1 1-1h3.5c.6 0 1 .4 1 1 0 1.3.2 2.5.6 3.6.1.3 0 .7-.2 1z"/></svg>
    <span>661-555-0173</span>
  </div>
  <h1 class="abs hero-title">Precision Sharpening.<br>Professional Results.</h1>
  <p class="abs hero-text">Restore your knives, scissors, and garden tools to peak performance with expert sharpening from Bay Bolt.</p>
  <div class="abs btn btn-red" style="top:405px;left:131px;width:148px;height:36px">
    <span>&#9742; Call Now</span>
  </div>
  <div class="abs btn btn-white" style="top:405px;left:286px;width:148px;height:36px"><span>View Services</span></div>
</header>
<div class="abs hero-band" style="left:0;width:1200px"></div>

<section style="top:585px;height:1400px">
  <h2 class="abs section-title" style="top:70px">What We Sharpen</h2>

  <article class="abs sharpen-card" style="top:175px;left:131px;height:445px">
    <h3>Kitchen Knives</h3>
    <div class="photo" role="img" aria-label="Set of kitchen knives on dark slate" style="height:163px;background:linear-gradient(135deg,#1a1a1a,#4a4a4a 50%,#1c1c1c)"></div>
    <p class="lead">Keep your kitchen performing at its best.</p>
    <ul class="ticks"><li>Chef knives</li><li>Paring knives</li><li>Serrated knives</li><li>Santoku knives</li><li>Cleavers</li></ul>
  </article>
  <article class="abs sharpen-card" style="top:179px;left:450px;height:445px">
    <h3>Scissors &amp; Shears</h3>
    <div class="photo" role="img" aria-label="Assorted scissors and shears on a dark surface" style="height:163px;background:linear-gradient(135deg,#222,#555 50%,#2a2a2a)"></div>
    <p class="lead">Clean, precise cuts<br>every time.</p>
    <ul class="ticks"><li>Kitchen scissors</li><li>Fabric shears</li><li>Hair cutting scissors</li><li>Utility scissors</li></ul>
  </article>
  <article class="abs sharpen-card" style="top:183px;left:769px;height:445px">
    <h3>Garden Tools</h3>
    <div class="photo" role="img" aria-label="Garden shears and tools laid on weathered wood" style="height:163px;background:linear-gradient(135deg,#2a2520,#5a5248 50%,#2a2620)"></div>
    <p class="lead">Sharp tools make gardening easier and safer.</p>
    <ul class="ticks"><li>Pruning shears</li><li>Hedge clippers</li><li>Shovels</li><li>Loppers</li><li>Axes &amp; garden blades</li></ul>
  </article>

  <h2 class="abs section-title" style="top:710px;text-transform:none">Sharper Than Ever</h2>
  <p class="abs" style="top:782px;left:330px;width:540px;text-align:center;font-size:14px;line-height:19px;color:var(--ink)">Every blade loses its edge over time. At Bay Bolt, we professionally restore, reshape, and sharpen your knives, scissors, and garden tools to peak performance.</p>
  <div class="abs btn btn-red" style="top:853px;left:528px;width:144px;height:37px"><span>&#9742; Call Now</span></div>
</section>

<div class="abs compare" role="img" aria-label="Before and after comparison of a dull and a freshly sharpened chef knife on dark stone">
  <div class="divider"></div>
  <div class="handle"></div>
  <div class="tag" style="left:28px">Before</div>
  <div class="tag" style="right:28px">After</div>
</div>

<section style="top:1985px;height:940px">
  <h2 class="abs section-title" style="top:50px">Sharpening Price List</h2>

  <article class="abs price-card" style="top:152px;left:135px">
    <h3>Knives</h3>
    <div class="photo" role="img" aria-label="Kitchen knives on dark slate" style="background:linear-gradient(135deg,#111,#444 50%,#151515)"></div>
    <div class="price-band">$8 <small>each</small></div>
    <p class="deal">5+ Knives<br>10% OFF</p>
    <ul class="price-list"><li>Standard Kitchen Knives</li><li>Large Knives / Cleavers <b>$10</b></li><li>Serrated Knives</li></ul>
    <div class="btn btn-red"><span>Book Now</span></div>
  </article>
  <article class="abs price-card" style="top:152px;left:450px">
    <h3>Scissors</h3>
    <div class="photo" role="img" aria-label="Scissors and shears on a dark surface" style="background:linear-gradient(135deg,#1a1a1a,#4d4d4d 50%,#1f1f1f)"></div>
    <div class="price-band">$8 <small>each</small></div>
    <p class="deal">3+ Scissors<br>10% OFF</p>
    <ul class="price-list"><li>Kitchen Scissors</li><li>Fabric Shears <b>$12</b></li><li>Hair Cutting Scissors <b>$15</b></li></ul>
    <div class="btn btn-red"><span>Book Now</span></div>
  </article>
  <article class="abs price-card" style="top:152px;left:765px">
    <h3>Tools</h3>
    <div class="photo" role="img" aria-label="Garden shears on weathered wood" style="background:linear-gradient(135deg,#1f1b17,#4e463d 50%,#221e1a)"></div>
    <div class="price-band">$10 <small>each</small></div>
    <p class="deal">5+ Tools<br>10% OFF</p>
    <ul class="price-list" style="margin-top:2px"><li>Pruning Shears</li><li>Hedge Clippers</li><li>Shovel/Garden Blade <b>$12</b></li><li>Axe / Loppers</li></ul>
    <div class="btn btn-red"><span>Book Now</span></div>
  </article>
</section>

<section class="testimonial">
  <div class="abs arrow" style="left:138px;top:270px"><svg width="16" height="16" viewBox="0 0 16 16" fill="none" stroke="#fff" stroke-width="1.5"><path d="M13 8H3M7 4 3 8l4 4"/></svg></div>
  <div class="abs arrow" style="left:1022px;top:270px"><svg width="16" height="16" viewBox="0 0 16 16" fill="none" stroke="#fff" stroke-width="1.5"><path d="M3 8h10M9 4l4 4-4 4"/></svg></div>
  <p class="abs quote">My kitchen knives came back like new. The edge holds and the blade feels balanced again.</p>
  <div class="abs" role="img" aria-label="Customer portrait" style="left:495px;top:420px;width:50px;height:50px;border-radius:50%;background:#c98a3a"></div>
  <p class="abs" style="left:556px;top:425px;font-size:12px;font-weight:700">Dana Ruiz</p>
  <p class="abs" style="left:556px;top:449px;font-size:11px">Home cook, Stevenson Ranch</p>
</section>

<h2 class="abs section-title" style="top:3650px;text-transform:none">Bring your tools in today</h2>
<p class="abs" style="top:3710px;left:0;width:1200px;text-align:center;font-size:13px;line-height:23px">Have dull knives, scissors, or garden tools?<br>We're ready to restore them to razor-sharp performance.</p>

<div class="abs contact-media">
  <div role="img" aria-label="Chef in white jacket holding up a large kitchen knife" style="height:438px;background:linear-gradient(90deg,#1a1a1a 0%,#2a2a2a 60%,#d8d8d8 100%);position:relative">
    <div class="brand" style="position:absolute;left:40px;top:186px;font-size:54px">Bay Bolt</div>
  </div>
  <div class="abs info-icon" style="left:40px;top:458px"><svg width="20" height="16" viewBox="0 0 20 16" fill="none" stroke="#fff" stroke-width="2"><rect x="1" y="1" width="18" height="14" rx="2"/><path d="m1 2 9 7 9-7"/></svg></div>
  <div class="abs info-title" style="left:38px;top:522px">Office Email</div>
  <div class="abs info-text" style="left:38px;top:560px">support@baybolt.com</div>
  <div class="abs info-icon" style="left:269px;top:458px"><svg width="16" height="20" viewBox="0 0 16 20" fill="#fff"><path d="M8 0a8 8 0 0 0-8 8c0 6 8 12 8 12s8-6 8-12a8 8 0 0 0-8-8zm0 11a3 3 0 1 1 0-6 3 3 0 0 1 0 6z"/></svg></div>
  <div class="abs info-title" style="left:267px;top:522px">Our Location</div>
  <div class="abs info-text" style="left:267px;top:560px">18302 Pellman Way,<br>Stevenson Ranch, CA 91381</div>
</div>

<form class="abs form-card">
  <h3 class="abs" style="left:44px;top:48px;font-family:'Oswald',sans-serif;font-weight:400;font-size:24px">Send a Message</h3>
  <label style="left:44px;top:116px">First Name*</label>
  <label style="left:244px;top:116px">Last Name*</label>
  <div class="field" style="left:44px;top:140px;width:186px;height:38px">First Name</div>
  <div class="field" style="left:244px;top:140px;width:186px;height:38px">Last Name</div>
  <label style="left:44px;top:196px">Phone Number*</label>
  <div class="field" style="left:44px;top:219px;width:386px;height:38px">Phone Number</div>
  <label style="left:44px;top:276px">Email Address*</label>
  <div class="field" style="left:44px;top:300px;width:386px;height:38px">Email Address</div>
  <label style="left:44px;top:356px">Short Message*</label>
  <div class="field" style="left:44px;top:378px;width:386px;height:135px">How Can We Help You?</div>
  <div class="abs btn btn-red" style="left:48px;top:544px;width:154px;height:36px"><span>Send Message</span></div>
</form>

<footer class="site-footer">
  <div class="abs brand" style="left:129px;top:88px;font-size:40px">Bay Bolt</div>
  <p class="abs" style="left:127px;top:182px;width:250px;font-size:14px;line-height:20px">Bring your tools in and let us professionally restore them to razor-sharp perfection.</p>
  <h4 class="abs footer-head" style="left:535px;top:84px">Quick Links</h4>
  <ul class="abs footer-links" style="left:535px;top:124px"><li>Home</li><li>About</li><li>Services</li><li>Pricing</li></ul>
  <h4 class="abs footer-head" style="left:735px;top:84px">Contact Us</h4>
  <div class="abs" style="left:736px;top:134px;display:flex;gap:14px;font-size:13px;align-items:center"><svg width="14" height="14" viewBox="0 0 24 24" fill="#fff"><path d="M6.6 10.8a15 15 0 0 0 6.6 6.6l2.2-2.2c.3-.3.7-.4 1-.2 1.1.4 2.3.6 3.6.6.6 0 1 .4 1 1V20c0 .6-.4 1-1 1A17 17 0 0 1 3 4c0-.6.4-1 1-1h3.5c.6 0 1 .4 1 1 0 1.3.2 2.5.6 3.6.1.3 0 .7-.2 1z"/></svg>661-555-0173</div>
  <div class="abs" style="left:736px;top:176px;display:flex;gap:14px;font-size:13px;line-height:19px;align-items:center"><svg width="12" height="16" viewBox="0 0 16 20" fill="#fff"><path d="M8 0a8 8 0 0 0-8 8c0 6 8 12 8 12s8-6 8-12a8 8 0 0 0-8-8zm0 11a3 3 0 1 1 0-6 3 3 0 0 1 0 6z"/></svg><span>18302 Pellman Way, Stevenson<br>Ranch, CA 91381</span></div>
  <div class="abs" style="left:736px;top:235px;display:flex;gap:14px;font-size:16px;align-items:center"><svg width="15" height="12" viewBox="0 0 20 16" fill="#fff"><path d="M0 2a2 2 0 0 1 2-2h16a2 2 0 0 1 2 2v.5l-10 7-10-7z M0 5l10 7 10-7v9a2 2 0 0 1-2 2H2a2 2 0 0 1-2-2z"/></svg>support@baybolt.com</div>
  <div class="abs social" style="left:1057px;top:140px"></div>
  <div class="abs social" style="left:1057px;top:175px;border-radius:50%"></div>
  <div class="abs social" style="left:1057px;top:210px"></div>
  <div class="abs social" style="left:1057px;top:244px;border-radius:50%"></div>
</footer>
<div class="abs copyright" style="left:0;width:1200px">© 2026 Bay Bolt. All rights reserved.</div>

</body>
</html>
```